Professional Single Page Website Design for Velloway Advisory

Velloway Advisory is a new business consultancy specializing in providing expert services to small businesses, primarily in the brick-and-mortar retail and food service sectors. We offer a range of services including franchise development and launch, due diligence, and construction management.

Currently, we have a basic website set up at www.vellowayadvisory.example, but we need a professional touch to enhance its design and functionality.

Project Requirements:
- Single Page Design: For now, we need a single page design that effectively showcases who we are, our services, and contact information.
- Future Expansion: The design should be flexible and scalable for future expansion to include additional pages like specific service offerings, about us, and a dedicated contact page.
- Design Aesthetic: We are looking for a modern yet professional design that aligns with our brand identity.
- Logo: We have a logo that we like, which was also sourced from Pixel Forum. The logo files are attached to this project brief.

Key Sections to Include:
- Hero Section: An engaging introduction to Velloway Advisory with a strong visual impact.
- About Us: A brief overview of who we are and our mission.
- Team: Section for the profiles of the two principals.
- Services: A clear and concise presentation of our services, including franchise development, due diligence, and construction management.
- Contact Information: Easy-to-find contact details, including a form for inquiries.
- Call to Action: Encouraging visitors to get in touch with us for consultations or further information.

Design Considerations:
- Ensure the design is responsive and mobile-friendly.
- Include high-quality images and icons that complement our services and industry.
- We do not need development services, this is only a design project.

```html
<!DOCTYPE html>
<html lang="en">
<head>
<meta charset="utf-8">
<title>Velloway Advisory</title>
<link href="https://fonts.googleapis.com/css2?family=Poppins:wght@400;500;600;700&family=Open+Sans:wght@400;600;700&display=swap" rel="stylesheet">
<style>
:root{
  --accent:#9bcfb2;
  --ink:#2f2f2f;
  --body:#5a5a5a;
  --cream:#f8f7f1;
  --line:#d9d9d9;
  --footer:#262b34;
  --footer-line:#3a404a;
  --white:#ffffff;
}
*{box-sizing:border-box;margin:0;padding:0}
html,body{width:1200px;height:4823px;overflow:hidden}
body{position:relative;background:var(--white);font-family:"Open Sans",Arial,sans-serif;color:var(--body)}
.abs{position:absolute;display:block}
.center{left:0;width:1200px;text-align:center}
.h2{font-family:"Poppins",Arial,sans-serif;font-weight:400;font-size:28px;color:var(--ink)}
.lead{font-size:14.5px;line-height:26px;color:var(--body)}

/* hero */
.hero{top:0;left:0;width:1200px;height:635px;overflow:hidden}
.hero-photo{position:absolute;left:0;top:0;width:1200px;height:635px;background:
  linear-gradient(180deg,rgba(20,40,80,.25),rgba(10,20,40,.35)),
  radial-gradient(ellipse at 50% 100%,#c98a3c 0%,rgba(201,138,60,0) 45%),
  linear-gradient(180deg,#2c5d9a 0%,#5d88b8 35%,#3b4f6a 65%,#6b4a2a 100%)}
.brand{left:38px;top:32px;display:flex;align-items:center;gap:10px;color:var(--white);font-family:"Poppins",sans-serif;font-weight:600;font-size:17px;line-height:19px}
.brand-mark{width:32px;height:32px;border:3px solid var(--white);border-radius:50%}
.menu-dots{right:30px;top:30px;width:26px;height:26px;display:grid;grid-template-columns:repeat(3,6px);gap:4px}
.menu-dots span{width:6px;height:6px;background:var(--white);border-radius:1px}
.hero-title{top:218px;font-family:"Poppins",sans-serif;font-weight:700;font-size:45px;line-height:50px;letter-spacing:2px;color:var(--white);text-transform:uppercase}
.hero-sub{top:330px;font-family:"Poppins",sans-serif;font-weight:600;font-size:24px;letter-spacing:1px;color:var(--white);text-transform:uppercase}
.hero-text{top:413px;font-size:14.5px;line-height:20px;color:var(--white)}

/* project */
.video{position:absolute;left:167px;top:863px;width:866px;height:449px;overflow:hidden}
.video-photo{position:absolute;left:0;top:0;width:866px;height:449px;background:radial-gradient(ellipse at 40% 50%,#e9d98a 0%,#c9b45a 30%,#6e6250 60%,#3d3a36 100%)}
.play{position:absolute;left:380px;top:164px;width:106px;height:106px;background:rgba(255,255,255,.92);border-radius:12px}
.controls{position:absolute;left:0;bottom:0;width:866px;height:26px;background:#1d1f24;display:flex;align-items:center;font-size:9px;color:#bbb}
.controls .pbtn{width:28px;height:26px;background:#2b8fd4}
.controls .bar{position:relative;flex:1;height:4px;background:#3a3d44;margin:0 12px}
.controls .bar i{position:absolute;left:0;top:0;width:100px;height:4px;background:#d33a5a}

/* who */
.who{top:1411px;left:0;width:1200px;height:592px;background:var(--cream)}
.person{left:116px;top:1385px;width:386px;height:618px;background:linear-gradient(180deg,#c9b8a8 0%,#3b2a36 25%,#2a1d28 100%);border-radius:150px 150px 0 0}
.who-title{left:597px;top:1498px}
.who-lead{left:597px;top:1560px;width:520px;font-size:14px;line-height:22px}
.feature{left:597px;width:520px}
.feature .ic{position:absolute;left:0;top:10px;width:44px;height:44px;border-radius:50%;background:var(--accent)}
.feature h3{margin-left:76px;font-size:16px;font-weight:700;color:var(--ink);margin-bottom:6px}
.feature p{margin-left:76px;font-size:12.5px;line-height:18px}
.dots{left:570px;top:1941px;display:flex;gap:10px}
.dots span{width:11px;height:11px;border-radius:50%;background:#b9b9b9}
.dots span:first-child{background:var(--accent)}

/* services */
.service{width:310px}
.service .num{display:inline-block;width:42px;height:42px;background:var(--accent);color:var(--white);font-family:"Poppins",sans-serif;font-size:26px;text-align:center;line-height:42px;vertical-align:middle}
.service h3{display:inline-block;margin-left:18px;font-family:"Poppins",sans-serif;font-weight:400;font-size:18px;color:var(--ink);vertical-align:middle}
.service p{margin-top:24px;font-size:12.5px;line-height:23px}
.service a{display:block;margin-top:8px;font-size:14px;color:var(--accent);text-decoration:none}

/* teams */
.teams{top:2720px;left:0;width:1200px;height:665px;background:var(--cream)}
.avatar{top:3058px;width:128px;height:128px;border-radius:50%;background:linear-gradient(180deg,#d9d4cf,#7a736c)}
.chat-btn{left:535px;top:3255px;width:128px;height:34px;background:var(--accent);color:var(--white);font-size:14px;font-weight:700;line-height:34px;text-align:center}

/* contact */
.col-title{font-family:"Poppins",sans-serif;font-weight:400;font-size:20px;color:var(--ink)}
.field-label{left:101px;font-size:12.5px;color:var(--ink)}
.field-label b{color:#e26b6b;font-weight:400}
.field{left:101px;width:481px;height:36px;border:1px solid var(--line);background:var(--white)}
.send{left:103px;top:4160px;width:105px;height:31px;background:var(--accent);color:var(--white);font-size:14px;font-weight:700;letter-spacing:1px;text-align:center;line-height:31px}
.info{left:661px;width:460px;font-size:12.5px;line-height:27px}
.info a{color:var(--accent);text-decoration:none}
.ci{left:664px;width:430px}
.ci svg{position:absolute;left:0;top:0}
.ci h4{margin-left:53px;font-size:13.5px;font-weight:400;color:var(--ink);margin-bottom:3px}
.ci p{margin-left:53px;font-size:12.5px;line-height:18px;color:var(--ink)}
.divider{left:139px;top:4259px;width:934px;height:1px;background:var(--line)}
.partners{left:150px;top:4360px;width:900px;display:flex;justify-content:space-between;align-items:center}
.partner{display:flex;align-items:center;gap:8px;font-family:"Poppins",sans-serif;font-weight:600;font-size:16px;color:#2a2a2a}
.partner i{width:14px;height:14px;background:#2a2a2a;border-radius:50%}

/* footer */
.footer{top:4543px;left:0;width:1200px;height:280px;background:var(--footer)}
.ft-title{font-family:"Poppins",sans-serif;font-weight:500;font-size:17px;letter-spacing:2px;color:var(--white)}
.ft-rule{height:2px;width:65px;background:var(--accent)}
.sub-input{left:92px;top:4661px;width:404px;height:36px;background:var(--white);font-size:10px;color:#aaa;line-height:36px;padding-left:16px}
.sub-btn{left:496px;top:4661px;width:92px;height:36px;background:var(--accent);color:var(--white);font-size:14px;font-weight:600;line-height:36px;text-align:center}
.socials{right:103px;top:4662px;display:flex;gap:12px}
.socials span{width:21px;height:21px;border-radius:50%;background:var(--accent)}
.ft-line{left:0;top:4755px;width:1200px;height:1px;background:var(--footer-line)}
.copyright{left:88px;top:4782px;font-size:11px;color:#cfd2d6}
.copyright span{color:var(--accent)}
.ft-links{right:88px;top:4782px;display:flex;gap:18px;font-size:11px;color:#cfd2d6}
</style>
</head>
<body>

<section class="hero abs">
  <div class="hero-photo" role="img" aria-label="Downtown skyline of glass towers at dusk"></div>
  <div class="brand abs" style="display:flex"><span class="brand-mark"></span><span>Velloway<br>Advisory</span></div>
  <div class="menu-dots abs" style="display:grid"><span></span><span></span><span></span><span></span><span></span><span></span><span></span><span></span><span></span></div>
  <h1 class="hero-title abs center">Building Success<br>In Southern California</h1>
  <p class="hero-sub abs center">Expertise at every step: from planning to execution</p>
  <p class="hero-text abs center">At Velloway, we blend innovative strategies with local market expertise to guide your commercial real estate ventures.<br>Whether you're launching a new restaurant, investing in retail spaces, or expanding a franchise,<br>our dedicated team is here to turn your real estate aspirations into tangible success.<br>Dive into a partnership that grows with you.</p>
</section>

<h2 class="h2 abs center" style="top:722px">Our Project</h2>
<p class="lead abs center" style="top:783px">Lorem ipsum dolar sit amet voluptatem fugit aut illo magni omnis explcabo ipsa nemo ipsam quasi illo dolores ut voluptatem<br>perspiciatis beatae architecto odit ipsa aspernatur magni qua aperiam aut veritatis beatae eos aut doloremque</p>
<div class="video">
  <div class="video-photo" role="img" aria-label="Construction team in hard hats reviewing building plans"></div>
  <div class="play"><svg width="106" height="106"><path d="M40 32 L76 53 L40 74 Z" fill="#e3262d"/></svg></div>
  <div class="controls"><span class="pbtn"></span><span style="margin-left:10px">00:15:55</span><span class="bar"><i></i></span><span style="margin-right:14px">2:15:35</span></div>
</div>

<section class="who abs"></section>
<div class="person abs" role="img" aria-label="Portrait of a principal in a dark suit"></div>
<h2 class="h2 abs who-title">Who We Are</h2>
<p class="abs who-lead">Lorem ipsum dolar sit amet voluptatem fugit aut illo omnis explicabo nemo ipsam quasi illo dolores eos voluptas voluptatem doloremque perspiciatis.</p>
<div class="abs feature" style="top:1636px">
  <span class="ic"><svg width="44" height="44"><ellipse cx="22" cy="16" rx="8" ry="3" fill="none" stroke="#fff" stroke-width="2"/><path d="M14 16v12c0 2 4 3 8 3s8-1 8-3V16M14 22c0 2 4 3 8 3s8-1 8-3" fill="none" stroke="#fff" stroke-width="2"/></svg></span>
  <h3>Voluptas Doloremque</h3>
  <p>Lorem ipsum dolar sit amet voluptatem fugit aut illo omnis explicabo nemo rem ipsam quasi illo dolores ut voluptatem doloremque perspiciatis beatae magni architecto odit odit, aspernatur magni quae aperiam aut veritatis beatae eos aut voluptas doloremque</p>
</div>
<div class="abs feature" style="top:1773px">
  <span class="ic"><svg width="44" height="44"><rect x="13" y="14" width="18" height="16" rx="2" fill="none" stroke="#fff" stroke-width="2"/><path d="M13 19h18" stroke="#fff" stroke-width="2"/></svg></span>
  <h3>Perspiciatis Beatae</h3>
  <p>Lorem ipsum dolar sit amet voluptatem fugit aut illo omnis explicabo nemo rem ipsam quasi illo dolores voluptatem doloremque perspiciatis beatae magni architecto odit odit, aspernatur magni quae aperiam aut veritatis beatae eos aut voluptas</p>
</div>
<div class="dots abs" style="display:flex"><span></span><span></span><span></span></div>

<h2 class="h2 abs center" style="top:2094px">Our Services</h2>
<p class="lead abs center" style="top:2153px;line-height:22px">Lorem ipsum dolar sit amet voluptatem fugit aut illo omnis explicabo ipsa nemo ipsam quasi illo dolores eos voluptas voluptatem<br>doloremque perspiciatis.</p>

<div class="service abs" style="left:95px;top:2267px"><span class="num">1</span><h3>Integrity And Morals</h3><p>Lorem ipsum dolor sit amet rem illo omnis aperiam ab ipsam ipsa odit aut aperiam aspernatur veritatis unde enim accusantium laudantium laudantiu sunt</p><a href="#">Read More</a></div>
<div class="service abs" style="left:449px;top:2267px"><span class="num">2</span><h3>Openness</h3><p>Lorem ipsum dolor sit amet rem illo omnis aperiam ab ipsam ipsa odit aut aperiam aspernatur veritatis unde enim accusantium laudantium laudantiu sunt</p><a href="#">Read More</a></div>
<div class="service abs" style="left:801px;top:2267px"><span class="num">3</span><h3>Responsibility</h3><p>Lorem ipsum dolor sit amet rem illo omnis aperiam ab ipsam ipsa odit aut aperiam aspernatur veritatis unde enim accusantium laudantium laudantiu sunt</p><a href="#">Read More</a></div>
<div class="service abs" style="left:95px;top:2473px"><span class="num">4</span><h3>People First</h3><p>Lorem ipsum dolor sit amet rem illo omnis aperiam ab ipsam ipsa odit aut aperiam aspernatur veritatis unde enim accusantium laudantium laudantiu sunt</p><a href="#">Read More</a></div>
<div class="service abs" style="left:449px;top:2473px"><span class="num">5</span><h3>Quality</h3><p>Lorem ipsum dolor sit amet rem illo omnis aperiam ab ipsam ipsa odit aut aperiam aspernatur veritatis unde enim accusantium laudantium laudantiu sunt</p><a href="#">Read More</a></div>
<div class="service abs" style="left:801px;top:2473px"><span class="num">6</span><h3>Safety</h3><p>Lorem ipsum dolor sit amet rem illo omnis aperiam ab ipsam ipsa odit aut aperiam aspernatur veritatis unde enim accusantium laudantium laudantiu sunt</p><a href="#">Read More</a></div>

<section class="teams abs"></section>
<h2 class="h2 abs center" style="top:2808px">We Have Great Teams</h2>
<p class="abs center" style="top:2882px;font-size:16.5px;line-height:29px">Lorem ipsum dolar sit amet voluptatem fugit aut illo omnis explcabo ipsa nemo rem ipsam quasi illo dolores<br>ut voluptatem doloreumque perspiciatis beatae magni architecto odit ipsa aspernatur magni qua<br>aperiam aut veritatis beatae eos aut volupt doloremque perspiciatis</p>
<div class="avatar abs" style="left:295px" role="img" aria-label="Team member portrait"></div>
<div class="avatar abs" style="left:535px" role="img" aria-label="Team member portrait"></div>
<div class="avatar abs" style="left:775px" role="img" aria-label="Team member portrait"></div>
<div class="chat-btn abs">Chat With Us</div>

<h2 class="h2 abs center" style="top:3476px">Contact Us</h2>
<p class="abs center" style="top:3553px;font-size:18px">Voluptatem doloremque perspi beatae quia ratione ratione beatae quia ratione ratione dolores</p>

<h3 class="col-title abs" style="left:101px;top:3652px">Contact Form</h3>
<label class="field-label abs" style="top:3699px">Name <b>*</b></label>
<div class="field abs" style="top:3722px"></div>
<label class="field-label abs" style="top:3783px">Email <b>*</b></label>
<div class="field abs" style="top:3806px"></div>
<label class="field-label abs" style="top:3865px">Subject <b>*</b></label>
<div class="field abs" style="top:3888px"></div>
<label class="field-label abs" style="top:3948px">How can i help <b>*</b></label>
<div class="field abs" style="top:3971px;height:155px"></div>
<div class="send abs">Send</div>

<h3 class="col-title abs" style="left:661px;top:3652px">Nice to hear from you</h3>
<p class="info abs" style="top:3694px">Lorem ipsum dolar sit amet voluptatem fugit aut illo omnis explicabo ipsa nemo rem ipsam quasi illo dolores ut voluptatem doloremque perspiciatis magni architecto odit aspernatur magni quae <a href="#">read more</a></p>
<h3 class="col-title abs" style="left:661px;top:3804px">Contact information</h3>

<div class="ci abs" style="top:3848px">
  <svg width="26" height="26"><circle cx="13" cy="13" r="13" fill="#8cc63f"/><circle cx="13" cy="13" r="6" fill="none" stroke="#fff" stroke-width="2"/><path d="M13 10v3h2" stroke="#fff" stroke-width="1.5" fill="none"/></svg>
  <h4>Business hours</h4>
  <p>Rem eos illo omnis aut aperiam ab ipsam ipsa odit aut<br>aperiam aut aspernatur veritatis.<br>Saturday : 10.00 to 18.00<br>Sunday : Close</p>
</div>
<div class="ci abs" style="top:3977px">
  <svg width="26" height="26"><circle cx="13" cy="13" r="13" fill="#e4533a"/><path d="M13 6a5 5 0 0 1 5 5c0 4-5 9-5 9s-5-5-5-9a5 5 0 0 1 5-5z" fill="#fff"/><circle cx="13" cy="11" r="2" fill="#e4533a"/></svg>
  <h4>Building address</h4>
  <p>Company Name<br>218 Harbor Crest Way<br>San Diego , California , 92199<br>Contractor License # 400218</p>
</div>
<div class="ci abs" style="top:4098px">
  <svg width="26" height="26"><circle cx="13" cy="13" r="13" fill="#d1528e"/><rect x="7" y="9" width="12" height="8" fill="#fff"/><path d="M7 9l6 5 6-5" stroke="#d1528e" stroke-width="1.2" fill="none"/></svg>
  <h4>Email</h4>
  <p>hello@vellowayadvisory.example</p>
</div>
<div class="ci abs" style="top:4163px">
  <svg width="26" height="26"><circle cx="13" cy="13" r="13" fill="#2f9fd8"/><path d="M9 7l3 0 1 3-2 1.5a8 8 0 0 0 3.5 3.5L16 13l3 1v3c-6 0-10-4-10-10z" fill="#fff"/></svg>
  <h4>Cellphone</h4>
  <p>(555) 014-2270</p>
</div>

<div class="divider abs"></div>
<div class="partners abs" style="display:flex">
  <span class="partner"><i></i>Lumen Cellar</span>
  <span class="partner"><i></i>Birch Echo</span>
  <span class="partner"><i></i>Pebble Kids</span>
  <span class="partner"><i></i>Framewise</span>
  <span class="partner"><i></i>Corner Bakehouse</span>
</div>

<footer class="footer abs"></footer>
<h4 class="ft-title abs" style="left:92px;top:4612px">Subscribe</h4>
<div class="ft-rule abs" style="left:92px;top:4642px"></div>
<div class="sub-input abs">your email address</div>
<div class="sub-btn abs">Sign Up</div>
<h4 class="ft-title abs" style="right:92px;top:4612px;font-size:15px">GET IN TOUCH</h4>
<div class="ft-rule abs" style="right:92px;top:4642px"></div>
<div class="socials abs" style="display:flex" aria-label="Social links"><span></span><span></span><span></span><span></span><span></span><span></span><span></span><span></span></div>
<div class="ft-line abs"></div>
<p class="copyright abs">© &nbsp;Copyright 2024 <span>Company Name Here</span> Inc.</p>
<nav class="ft-links abs" style="display:flex"><span>Home</span><span>Contact Us</span><span>Privacy Notice</span></nav>

</body>
</html>
```